Vitamin/Dietary Supplement Company needs a simple Hemp CBD Health retail website to display a few...

We need a simple website designed that will allow us to display a few products for purchase. We are a vitamin/dietary supplement company that wants to set up a separate website for CBD health products. CBD is a chemical compound found in hemp and cannabis plants that provide various health and medicinal benefits. Our target audience are individuals that suffer from health issues and would like to treat their pain relief with CBD as an alternative to prescription medication and over the counter drugs such as Paxorin and Dolvex. Looking for a simple and clean website that is easy for customers to navigate and purchase products.

Need extra days to review

Target Market(s)

Our target audience are individuals that suffer from health issues and would like to treat their pain relief with CBD as an alternative to prescription medication and over the counter drugs such as Paxorin and Dolvex.

Coding

Coded - Design and coding required

Font styles to use
Serif

Colors

Designer to choose colors to be used in the design.

Requirements
Nice to have
• Homepage, About page, FAQ page, Contact page, Blog page

```html
<!DOCTYPE html>
<html lang="en">
<head>
<meta charset="utf-8">
<title>CalmLeaf – CBD Health Store</title>
<link rel="stylesheet" href="https://fonts.googleapis.com/css2?family=Lora:wght@400;600;700&family=Merriweather:wght@700;900&display=swap">
<style>
:root{
  --green:#8cc43f;
  --green-dark:#6fa82a;
  --green-pale:#e3f0cf;
  --green-soft:#d2e8b2;
  --blue:#2f45d6;
  --blue-soft:#6f7fe6;
  --navy:#1b2a8f;
  --ink:#222;
  --text:#555;
  --muted:#999;
  --line:#d9d9d9;
  --header-bg:#f3f3f1;
  --band-bg:#eef3f6;
  --footer-bg:#eef1f4;
  --bottom-bg:#3b3b3b;
  --orange:#f2a21e;
  --white:#fff;
}
*{box-sizing:border-box;margin:0;padding:0}
html,body{width:1200px;height:2975px;overflow:hidden;background:var(--white)}
body{font-family:"Lora",Georgia,serif;color:var(--text);position:relative}

/* header */
.site-header{position:absolute;left:0;top:0;width:1200px;height:110px;background:var(--header-bg)}
.topbar{position:absolute;left:246px;top:8px;width:716px;height:20px;border-bottom:1px solid var(--line);font-size:8px;color:#666;display:flex;align-items:center}
.topbar .hotline{width:160px}
.topbar .social{display:flex;gap:7px;width:120px}
.topbar .social span{width:6px;height:6px;border-radius:50%;background:#777}
.topbar .account{display:flex;gap:12px}
.topbar .newsletter{margin-left:auto}
.logo{position:absolute;left:123px;top:38px;font-family:"Merriweather",Georgia,serif;font-weight:900;font-size:24px;color:var(--navy)}
.main-nav{position:absolute;left:514px;top:52px;display:flex;gap:16px;font-family:"Merriweather",Georgia,serif;font-weight:700;font-size:12px;color:var(--navy)}
.search-btn{position:absolute;left:935px;top:54px;width:20px;height:20px;border:1px solid #888;border-radius:2px}

/* hero */
.hero{position:absolute;left:0;top:110px;width:1190px;height:405px;background:var(--green-pale);overflow:hidden}
.hero svg.diag{position:absolute;left:0;top:0}
.hero-title{position:absolute;left:298px;top:46px;font-family:"Merriweather",Georgia,serif;font-weight:900;font-size:22px;color:var(--blue);letter-spacing:.3px}
.hero-sub{position:absolute;left:300px;top:88px;font-family:"Merriweather",Georgia,serif;font-weight:700;font-size:14px;color:var(--blue-soft)}
.hero-text{position:absolute;left:300px;top:128px;width:250px;font-size:8px;line-height:12px;color:#b7c9a0}
.hero-photo{position:absolute;left:590px;top:64px;width:300px;height:316px;border-radius:45%;background:radial-gradient(circle at 45% 50%,#b7dc86 0%,#8ec64b 40%,rgba(200,230,170,.3) 72%,rgba(227,240,207,0) 80%)}
.hero-arrow{position:absolute;top:172px;width:62px;height:62px;background:rgba(120,130,120,.55)}
.hero-arrow.prev{left:12px}.hero-arrow.next{left:1114px}
.hero-arrow svg{position:absolute;left:23px;top:23px}

/* features */
.features{position:absolute;left:250px;top:555px;width:700px;display:grid;grid-template-columns:repeat(4,175px)}
.feature{text-align:center}
.feature .icon{width:38px;height:38px;border:2px solid var(--green);border-radius:50%;margin:0 auto 14px;display:flex;align-items:center;justify-content:center}
.feature h3{font-size:12px;font-weight:400;color:var(--ink);margin-bottom:12px}
.feature p{font-size:9px;line-height:13px;color:#666;padding:0 8px}

/* section headings */
.section-head{position:absolute;left:270px;width:666px;height:14px;text-align:center}
.section-head::before{content:"";position:absolute;left:0;right:0;top:7px;border-top:1px solid #bbb}
.section-head span{position:relative;padding:0 12px;font-size:12px;color:var(--ink);letter-spacing:.3px}
.fresh-band{position:absolute;left:0;top:734px;width:1200px;height:318px;background:var(--band-bg)}
.on-band span{background:var(--band-bg)}
.on-white span{background:var(--white)}

/* product cards */
.card-row{position:absolute;left:270px;width:666px;display:grid;grid-template-columns:repeat(4,150px);gap:22px}
.card{height:200px;background:var(--white);border:1px solid #e1e1e1;position:relative;overflow:hidden}
.card .shot{height:150px;background:var(--white)}
.card .sale{position:absolute;right:0;top:0;width:38px;height:38px;background:var(--green);clip-path:polygon(0 0,100% 0,100% 100%)}
.card .sale b{position:absolute;right:1px;top:9px;transform:rotate(45deg);font-size:6px;color:#fff;font-weight:700}
.card .info{position:absolute;left:6px;right:8px;bottom:10px;height:34px}
.card .name{font-size:9px;color:var(--ink);white-space:nowrap}
.card .cat{font-size:7px;color:var(--muted);margin-top:3px;white-space:nowrap}
.card .old{position:absolute;right:0;top:0;font-size:7px;color:#bbb;text-decoration:line-through}
.card .price{position:absolute;right:0;bottom:0;font-size:17px;font-weight:700;color:var(--green)}
.shot.tincture{background:radial-gradient(ellipse 14% 30% at 50% 55%,#c98a2c 0,#8a5516 70%,#fff 100%)}
.shot.gummies{background:radial-gradient(circle at 50% 58%,#f0a83a 0,#d8672a 26%,#fff 40%)}
.shot.softgel{background:radial-gradient(ellipse 26% 16% at 50% 55%,#e2b94a 0,#b7861c 70%,#fff 100%)}
.shot.balm{background:radial-gradient(circle at 50% 55%,#a9d37a 0,#6fa82a 26%,#fff 40%)}
.shot.capsule{background:radial-gradient(ellipse 30% 14% at 50% 55%,#9fc86a 0,#5f8f2a 70%,#fff 100%)}
.shot.drops{background:linear-gradient(135deg,#fff 30%,#d9a24a 45%,#b8772a 55%,#fff 70%)}
.shot.leaf{background:radial-gradient(circle at 50% 50%,#3f8a28 0,#1f5b16 60%,#123c0d 100%)}
.cat-card .info{bottom:12px;text-align:center;left:0;right:0}
.divider{position:absolute;left:270px;width:666px;border-top:1px solid var(--line)}

/* promo banners */
.promo{position:absolute;top:1423px;height:134px;overflow:hidden}
.promo h3{position:absolute;left:14px;top:14px;font-family:"Merriweather",Georgia,serif;font-weight:700;font-size:18px}
.promo p{position:absolute;left:14px;top:46px;font-size:10px;line-height:13px}
.promo.tinctures{left:270px;width:322px;background:linear-gradient(90deg,#3b2a1c 0,#5a3d26 45%,#c9801f 65%,#b8661a 100%)}
.promo.tinctures h3{color:var(--orange)}
.promo.tinctures p{color:#eee}
.promo.gummies{left:609px;width:327px;background:linear-gradient(90deg,#c9c0b0 0,#e7e2d8 40%,#b78c5a 70%,#f0b021 100%)}
.promo.gummies h3{color:#3a3a3a}
.promo.gummies p{color:#555;width:120px}

/* shipping band */
.shipping{position:absolute;left:6px;top:1855px;width:1194px;height:274px;background:linear-gradient(90deg,#8bc43e,#9ccd52 55%,#86bf38)}
.shipping .scene{position:absolute;right:0;top:0;width:520px;height:274px;background:linear-gradient(100deg,rgba(140,196,63,0) 0,rgba(170,214,100,.55) 55%,rgba(120,170,50,.5) 100%)}
.shipping .truck{position:absolute;left:574px;top:76px}
.shipping h2{position:absolute;left:0;width:1180px;top:118px;text-align:center;font-family:"Merriweather",Georgia,serif;font-size:28px;font-weight:700;color:#fff}
.shipping p{position:absolute;left:0;width:1180px;top:178px;text-align:center;font-size:13px;line-height:19px;font-weight:700;color:#fff}

/* blog */
.posts{position:absolute;left:276px;top:2224px;width:660px;display:grid;grid-template-columns:330px 330px;row-gap:34px}
.post h4{font-size:11px;font-weight:400;color:var(--ink);margin-bottom:10px}
.post p{font-size:8.5px;line-height:12px;color:#666;width:310px}

/* product lists */
.lists{position:absolute;left:246px;top:2502px;width:550px;display:grid;grid-template-columns:repeat(3,183px)}
.lists h5{font-size:10px;font-weight:700;color:var(--ink);margin-bottom:8px}
.mini{position:relative;width:167px;height:61px;border:1px solid #e3e3e3;margin-bottom:3px;background:#fff}
.mini .thumb{position:absolute;left:0;top:0;width:60px;height:59px;border-right:1px solid #eee}
.mini .tag{position:absolute;left:0;top:0;width:20px;height:20px;background:var(--green);clip-path:polygon(0 0,100% 0,0 100%)}
.mini .name{position:absolute;left:68px;top:8px;font-size:10px;color:var(--ink);white-space:nowrap}
.mini .prices{position:absolute;right:8px;bottom:9px;display:flex;align-items:baseline;gap:4px}
.mini .old{font-size:7px;color:#bbb;text-decoration:line-through}
.mini .price{font-size:12px;font-weight:700;color:var(--green)}
.thumb.amber{background:radial-gradient(ellipse 14% 28% at 50% 55%,#c98a2c 0,#8a5516 70%,#fff 100%)}
.thumb.orange{background:radial-gradient(circle at 50% 55%,#f0a83a 0,#d8672a 24%,#fff 38%)}
.thumb.green{background:radial-gradient(circle at 50% 55%,#a9d37a 0,#6fa82a 24%,#fff 38%)}
.thumb.gold{background:radial-gradient(ellipse 26% 16% at 50% 55%,#e2b94a 0,#b7861c 70%,#fff 100%)}
.to-top{position:absolute;left:968px;top:2690px;width:30px;height:20px;background:#333;color:#fff;font-size:8px;font-weight:700;display:flex;align-items:center;justify-content:center;border-radius:2px}

/* footer */
.site-footer{position:absolute;left:0;top:2737px;width:1200px;height:190px;background:var(--footer-bg)}
.footer-cols{position:absolute;left:246px;top:22px;display:grid;grid-template-columns:182px 182px 182px 182px}
.footer-cols > div{width:168px}
.footer-cols h6{font-size:8.5px;font-weight:700;color:var(--ink);border-left:2px solid var(--green);padding-left:5px;margin-bottom:8px}
.footer-cols p,.footer-cols li{font-size:7.5px;line-height:10px;color:#777;list-style:none}
.footer-cols .date{color:#aaa;margin-bottom:4px}
.footer-cols label{font-size:7.5px;color:#777;display:block;margin-bottom:3px}
.footer-cols .field{width:130px;height:14px;background:#fff;border:1px solid #ddd;margin-bottom:8px}
.footer-cols .subscribe{width:130px;height:14px;background:var(--orange);color:#fff;font-size:7px;text-align:center;line-height:14px}
.footer-cols .sub-item{padding-left:10px}
.bottom-bar{position:absolute;left:0;top:2927px;width:1200px;height:48px;background:var(--bottom-bg)}
.pay{position:absolute;top:16px;display:flex;gap:7px;left:690px}
.pay span{width:24px;height:15px;background:#e9e9e9;border-radius:2px}
</style>
</head>
<body>

<header class="site-header">
  <div class="topbar">
    <div class="hotline">24/7 Hotline: 555 0142 300</div>
    <div class="social"><span></span><span></span><span></span><span></span><span></span><span></span><span></span><span></span></div>
    <div class="account"><span>English (en)</span><span>My Account</span><span>Cart</span><span>Wishlist</span></div>
    <div class="newsletter">Sign up to our newsletter!</div>
  </div>
  <div class="logo">CalmLeaf</div>
  <nav class="main-nav"><span>Home</span><span>About</span><span>FAQ</span><span>Contact</span><span>Blog</span></nav>
  <div class="search-btn">
    <svg width="18" height="18" viewBox="0 0 18 18"><circle cx="8" cy="8" r="3.5" fill="none" stroke="#555" stroke-width="1.3"/><line x1="10.5" y1="10.5" x2="13" y2="13" stroke="#555" stroke-width="1.3"/></svg>
  </div>
</header>

<section class="hero">
  <svg class="diag" width="1190" height="405" viewBox="0 0 1190 405"><polygon points="1190,0 1190,405 200,405" fill="var(--green-soft)"/></svg>
  <h1 class="hero-title">BEST CBD AND CALMING INFUSION</h1>
  <div class="hero-sub">BEST OFFER</div>
  <p class="hero-text">Pure hemp extract blended with soothing botanicals for calm, steady comfort through the whole day and night.</p>
  <div class="hero-photo" role="img" aria-label="Fresh green citrus with a leaf on a green paint splash"></div>
  <div class="hero-arrow prev"><svg width="16" height="16" viewBox="0 0 16 16"><polyline points="11,2 5,8 11,14" fill="none" stroke="#fff" stroke-width="2"/></svg></div>
  <div class="hero-arrow next"><svg width="16" height="16" viewBox="0 0 16 16"><polyline points="5,2 11,8 5,14" fill="none" stroke="#fff" stroke-width="2"/></svg></div>
</section>

<section class="features">
  <div class="feature">
    <div class="icon"><svg width="16" height="16" viewBox="0 0 16 16"><path d="M4 2l2 3-1.5 1.5c.8 2 2.5 3.7 4.5 4.5L10.5 9.5l3 2-1.5 2.5C7 13.5 2.5 9 2 3.5z" fill="var(--green)"/></svg></div>
    <h3>24 / 7 Hotline</h3>
    <p>Talk to our wellness team any hour about dosage, products and orders.</p>
  </div>
  <div class="feature">
    <div class="icon"><svg width="16" height="16" viewBox="0 0 16 16"><polygon points="9,1 4,9 8,9 7,15 12,7 8,7" fill="none" stroke="var(--green)" stroke-width="1.3"/></svg></div>
    <h3>Quick Delivery</h3>
    <p>Orders leave our warehouse within one day in discreet plain packaging.</p>
  </div>
  <div class="feature">
    <div class="icon"><svg width="16" height="16" viewBox="0 0 16 16"><ellipse cx="8" cy="8" rx="4" ry="6" fill="none" stroke="var(--green)" stroke-width="1.3"/><line x1="8" y1="4" x2="8" y2="14" stroke="var(--green)" stroke-width="1.3"/></svg></div>
    <h3>Lab Tested</h3>
    <p>Every batch is tested by an independent lab for purity and strength.</p>
  </div>
  <div class="feature">
    <div class="icon"><svg width="16" height="16" viewBox="0 0 16 16"><path d="M8 13L3 8a3 3 0 0 1 5-4 3 3 0 0 1 5 4z" fill="none" stroke="var(--green)" stroke-width="1.3"/></svg></div>
    <h3>100% Organic</h3>
    <p>Grown from organic hemp on family farms, free of pesticides and fillers.</p>
  </div>
</section>

<div class="fresh-band"></div>
<div class="section-head on-band" style="top:771px"><span>BEST SELLERS</span></div>
<div class="card-row" style="top:806px">
  <div class="card"><div class="shot tincture" role="img" aria-label="CBD oil dropper bottle"></div><div class="sale"><b>SALE</b></div><div class="info"><div class="name">CBD Oil 500mg</div><div class="cat">Tinctures</div><div class="old">$44.99</div><div class="price">$39.99</div></div></div>
  <div class="card"><div class="shot gummies" role="img" aria-label="CBD gummies in a jar"></div><div class="sale"><b>SALE</b></div><div class="info"><div class="name">Calm Gummies</div><div class="cat">Edibles, Sleep</div><div class="old">$29.99</div><div class="price">$24.99</div></div></div>
  <div class="card"><div class="shot softgel" role="img" aria-label="Hemp softgel capsules"></div><div class="info"><div class="name">Hemp Softgels</div><div class="cat">Capsules</div><div class="price">$34.99</div></div></div>
  <div class="card"><div class="shot balm" role="img" aria-label="Tin of CBD relief balm"></div><div class="sale"><b>SALE</b></div><div class="info"><div class="name">Relief Balm</div><div class="cat">Topicals</div><div class="old">$27.99</div><div class="price">$22.99</div></div></div>
</div>

<div class="section-head on-white" style="top:1096px"><span>SPECIAL OFFER</span></div>
<div class="card-row" style="top:1131px">
  <div class="card"><div class="shot capsule" role="img" aria-label="CBD capsules"></div><div class="sale"><b>SALE</b></div><div class="info"><div class="name">Daily Capsules</div><div class="cat">Capsules</div><div class="price">$29.99</div></div></div>
  <div class="card"><div class="shot drops" role="img" aria-label="Bottle of CBD drops"></div><div class="sale"><b>SALE</b></div><div class="info"><div class="name">Sleep Drops</div><div class="cat">Tinctures</div><div class="old">$39.99</div><div class="price">$32.99</div></div></div>
  <div class="card"><div class="shot balm" role="img" aria-label="Tin of CBD relief balm"></div><div class="sale"><b>SALE</b></div><div class="info"><div class="name">Relief Balm</div><div class="cat">Topicals</div><div class="price">$22.99</div></div></div>
  <div class="card"><div class="shot gummies" role="img" aria-label="CBD gummies in a jar"></div><div class="sale"><b>SALE</b></div><div class="info"><div class="name">Calm Gummies</div><div class="cat">Edibles, Sleep</div><div class="price">$24.99</div></div></div>
</div>

<div class="divider" style="top:1402px"></div>

<div class="promo tinctures" role="img" aria-label="Amber CBD oil bottles on a wooden table">
  <h3>Organic Tinctures</h3>
  <p>Cold pressed - gentle daily relief.</p>
</div>
<div class="promo gummies" role="img" aria-label="Bowl of CBD gummies">
  <h3>Calming Gummies</h3>
  <p>A tasty way to unwind every evening.</p>
</div>

<div class="section-head on-white" style="top:1594px"><span>CATEGORIES</span></div>
<div class="card-row" style="top:1631px">
  <div class="card cat-card"><div class="shot tincture" role="img" aria-label="CBD oil bottles"></div><div class="info"><div class="name">Tinctures</div><div class="cat">Items 6</div></div></div>
  <div class="card cat-card"><div class="shot gummies" role="img" aria-label="CBD gummies"></div><div class="info"><div class="name">Edibles</div><div class="cat">Items 7</div></div></div>
  <div class="card cat-card"><div class="shot balm" role="img" aria-label="CBD balms and creams"></div><div class="info"><div class="name">Topicals</div><div class="cat">Items 5</div></div></div>
  <div class="card cat-card"><div class="shot leaf" role="img" aria-label="Hemp plant leaves"></div><div class="info"><div class="name">Hemp Extracts</div><div class="cat">Items 8</div></div></div>
</div>

<section class="shipping">
  <div class="scene" role="img" aria-label="Delivery van on a country road beside green fields"></div>
  <svg class="truck" width="40" height="28" viewBox="0 0 40 28"><rect x="2" y="3" width="22" height="16" fill="none" stroke="#fff" stroke-width="2"/><path d="M24 8h8l5 6v5H24z" fill="none" stroke="#fff" stroke-width="2"/><circle cx="10" cy="22" r="3" fill="var(--green)" stroke="#fff" stroke-width="2"/><circle cx="30" cy="22" r="3" fill="var(--green)" stroke="#fff" stroke-width="2"/></svg>
  <h2>FREE SHIPPING ON ALL ORDERS OVER $99</h2>
  <p>We offer free shipping service on all orders over $99 including tax.<br>No matter where you are in the world.</p>
</section>

<div class="section-head on-white" style="top:2166px"><span>LATEST BLOG POSTS</span></div>
<section class="posts">
  <article class="post"><h4>How CBD may ease everyday pain</h4><p>Many of our customers look for gentle relief without reaching for Paxorin or Dolvex every day. Here is what current research says about hemp extract and comfort. [...]</p></article>
  <article class="post"><h4>Gallery Post</h4><p>This post shows a Swivel Slider gallery of our hemp farm and lab, from harvest to the finished bottle on your shelf. [...]</p></article>
  <article class="post"><h4>Videopost from ClipTube</h4><p>Watch our wellness team explain how to choose a strength, how to measure a dose and what to expect during the first weeks. [...]</p></article>
  <article class="post"><h4>Better Sleep Weeks</h4><p>Small evening habits paired with a calming tincture can help you wind down. We share five simple routines our readers love. [...]</p></article>
</section>
<div class="divider" style="top:2410px"></div>

<section class="lists">
  <div>
    <h5>TOPSELLERS</h5>
    <div class="mini"><div class="thumb amber" role="img" aria-label="CBD oil bottle"></div><div class="tag"></div><div class="name">CBD Oil 500mg</div><div class="prices"><span class="old">$44.99</span><span class="price">$39.99</span></div></div>
    <div class="mini"><div class="thumb orange" role="img" aria-label="CBD gummies"></div><div class="tag"></div><div class="name">Calm Gummies</div><div class="prices"><span class="old">$29.99</span><span class="price">$24.99</span></div></div>
    <div class="mini"><div class="thumb green" role="img" aria-label="Relief balm"></div><div class="tag"></div><div class="name">Relief Balm</div><div class="prices"><span class="old">$27.99</span><span class="price">$22.99</span></div></div>
  </div>
  <div>
    <h5>ON SALE</h5>
    <div class="mini"><div class="thumb amber" role="img" aria-label="Sleep drops bottle"></div><div class="tag"></div><div class="name">Sleep Drops</div><div class="prices"><span class="old">$39.99</span><span class="price">$32.99</span></div></div>
    <div class="mini"><div class="thumb orange" role="img" aria-label="CBD gummies"></div><div class="tag"></div><div class="name">Calm Gummies</div><div class="prices"><span class="old">$29.99</span><span class="price">$24.99</span></div></div>
    <div class="mini"><div class="thumb gold" role="img" aria-label="Hemp softgels"></div><div class="tag"></div><div class="name">Hemp Softgels</div><div class="prices"><span class="old">$38.99</span><span class="price">$34.99</span></div></div>
  </div>
  <div>
    <h5>FRESHLY ADDED</h5>
    <div class="mini"><div class="thumb green" role="img" aria-label="Muscle rub"></div><div class="name">Muscle Rub</div><div class="prices"><span class="price">$19.99</span></div></div>
    <div class="mini"><div class="thumb amber" role="img" aria-label="Sleep drops bottle"></div><div class="tag"></div><div class="name">Sleep Drops</div><div class="prices"><span class="old">$39.99</span><span class="price">$32.99</span></div></div>
    <div class="mini"><div class="thumb gold" role="img" aria-label="Daily capsules"></div><div class="tag"></div><div class="name">Daily Capsules</div><div class="prices"><span class="old">$34.99</span><span class="price">$29.99</span></div></div>
  </div>
</section>
<div class="to-top">TOP</div>

<footer class="site-footer">
  <div class="footer-cols">
    <div>
      <h6>ABOUT CALMLEAF</h6>
      <p>We make simple hemp products for people who want natural support for pain, stress and rest.</p>
      <p style="margin-top:8px">Questions about dosage? Our team is happy to help you pick the right product.</p>
    </div>
    <div>
      <h6>LATEST BLOG POSTS</h6>
      <p>How CBD may ease everyday pain</p><p class="date">November 6, 2014</p>
      <p>Gallery Post</p><p class="date">November 5, 2014</p>
      <p>Videopost from ClipTube</p><p class="date">November 4, 2014</p>
      <p>Better Sleep Weeks</p><p class="date">September 7, 2014</p>
    </div>
    <div>
      <h6>NEWSLETTER</h6>
      <label>Email Address</label>
      <div class="field"></div>
      <div class="subscribe">Subscribe</div>
    </div>
    <div>
      <h6>CATEGORIES</h6>
      <ul>
        <li>• Capsules</li><li>• Tinctures</li><li class="sub-item">• Sleep Drops</li><li>• Edibles</li><li>• Topicals</li><li>• Hemp Extracts</li><li>• Bundles</li><li>• Gift Sets</li>
      </ul>
    </div>
  </div>
</footer>
<div class="bottom-bar">
  <div class="pay"><span></span><span></span><span></span><span></span><span></span><span></span><span></span><span></span><span></span><span></span></div>
</div>

</body>
</html>
```